International Dental Education Website

This project is for a small teaching center on endodontic and micro dentistry in Norway. We need a Wordpress website design to display and highlight dental educational courses. Please use our new logo - see attached file. We like lighter, pastel oriented colors. The following sites are nicely laid out and you can use these as a guideline of sorts but I do want a unique site.
http://vorplex.example/en, http://www.toothmarlow.example/Education.aspx?currentSection=courses&cid=14,
http://www.pulpvesker.example/.
Please create a space for a possible video on the home page. Please include a small contact form on the home page(name, email, phone, text box). Would like a horizonatal naviagtion bar. Would like an image to go across the whole top part of the site and this may rotate. Please use a stock image that shows a classroom type setting. Put phone number at the top of the screen. Put address and sitemap in a footer.

Reason: Upcoming vacation with limited internet access. Please continue to submit any designs. Thanks you.

Reason: The client is from a foreign country and is on an extended vacation.

Target Market(s)

General dentists (GPs) and specialists in Endodontics

Industry/Entity Type

Dental

Requirements
Must have
• Sitemap: HOME, COURSES, LECTURER, CONTACT US,
NORWEGIAN/ENGLISH. Phone number is: +47 93516270. Business name and address: Kali Rom AS, Endodontic Teaching Center,
Fjeldstads vei 17C, 0371 Oslo, Norway.

```html
<!DOCTYPE html>
<html lang="en">
<head>
<meta charset="utf-8">
<title>Kali Rom – Endodontic Teaching Center</title>
<link rel="stylesheet" href="https://fonts.googleapis.com/css2?family=Didact+Gothic&family=Carlito:wght@400;700&family=Crimson+Text:ital@1&family=Open+Sans:wght@400;700;800&display=swap">
<style>
:root{
  --sky-top:#c6ecf3;
  --sky-bottom:#e4f5f9;
  --teal:#5ec0c4;
  --teal-dark:#2e9ea3;
  --purple:#9a8ed8;
  --purple-dark:#7669bd;
  --footer:#6b5cab;
  --footer-dark:#594a98;
  --ink:#444;
  --muted:#666;
  --panel:#ebebeb;
  --field:#f7f7f7;
  --beige:#e5e1c6;
  --tweet-blue:#3a9fd2;
  --white:#fff;
}
*{box-sizing:border-box;margin:0;padding:0}
html,body{width:825px;height:1200px;overflow:hidden}
body{position:relative;background:linear-gradient(180deg,var(--sky-top) 0,var(--sky-bottom) 700px,var(--sky-bottom) 1030px);font-family:"Carlito",sans-serif;color:var(--ink)}
.abs{position:absolute}
a{color:inherit;text-decoration:none}

/* header */
.brand{left:115px;top:26px;font-family:"Didact Gothic",sans-serif;font-size:26px;color:var(--teal);display:flex;align-items:center;gap:6px}
.brand-dot{width:10px;height:10px;border-radius:50%;background:var(--teal)}
.lang-label{left:436px;top:13px;font-size:11px;color:var(--muted)}
.lang-select{left:510px;top:11px;width:57px;height:17px;background:var(--white);border:1px solid #bbb;font-size:9px;padding:2px 4px}
.lang-select::after{content:"";position:absolute;right:0;top:0;width:14px;height:15px;background:var(--purple)}
.search{left:583px;top:11px;width:132px;height:17px;background:var(--white);border:1px solid #bbb;font-size:9px;padding:2px 5px}
.search::after{content:"";position:absolute;right:0;top:0;width:17px;height:15px;background:var(--purple)}
.follow{left:602px;top:50px;font-size:11px;color:var(--muted);display:flex;gap:5px;align-items:center}
.follow span.sq{width:16px;height:16px;border-radius:3px;background:var(--tweet-blue);display:inline-block}
.follow span.sq:first-of-type{margin-left:4px}

/* nav */
.nav{left:110px;top:86px;width:605px;height:37px;background:linear-gradient(180deg,#b3a8e6,var(--purple) 55%,var(--purple-dark));border-radius:2px;display:flex}
.nav a{font-family:"Didact Gothic",sans-serif;font-size:10.5px;color:var(--white);padding:12px 14px 0;height:37px;border-right:1px solid rgba(255,255,255,.25)}
.nav a.active{background:linear-gradient(180deg,#84d2d6,var(--teal));width:53px;padding-left:13px}
.nav a:nth-child(2){width:81px;padding-left:22px}
.nav a:nth-child(3){width:75px;padding-left:17px}
.nav a:nth-child(4){border:0}
.call{left:585px;top:88px;display:flex;gap:6px;color:var(--white)}
.call-label{font-family:"Open Sans",sans-serif;font-weight:800;font-size:10.5px;line-height:12px;color:#2a2440}
.call-num{font-family:"Open Sans",sans-serif;font-weight:700;font-size:15px;color:#2a2440;line-height:16px}

/* slider */
.slider{left:110px;top:137px;width:605px;height:265px;background:var(--teal);border-radius:3px;padding:7px 6px 5px}
.slide{position:relative;width:593px;height:253px;background:linear-gradient(180deg,#5f8a55,#b27868 50%,#3a3a44)}
.caption{position:absolute;left:0;bottom:0;width:100%;height:42px;background:rgba(20,20,30,.55);font-family:"Crimson Text",serif;font-style:italic;font-size:22px;color:var(--white);padding:6px 10px;white-space:nowrap;overflow:hidden}
.arrow{position:absolute;top:115px;width:24px;height:38px;background:var(--teal);display:flex;align-items:center;justify-content:center}
.arrow.prev{left:0;border-radius:0 20px 20px 0}
.arrow.next{right:0;border-radius:20px 0 0 20px}

/* main */
.main{left:110px;top:415px;width:605px;height:602px;background:var(--white);border-radius:3px}
.h-section{font-family:"Didact Gothic",sans-serif;color:var(--teal-dark);font-weight:400}
.intro-title{left:129px;top:430px;font-size:17px}
.intro{left:130px;top:456px;width:392px;font-size:10px;line-height:14.2px;color:var(--ink)}
.read-more{left:462px;top:513px;font-size:10.5px;color:var(--teal-dark)}
.series{width:181px;height:164px;background:#f4f4f4;border:1px solid #ddd;border-radius:3px;padding:8px 10px}
.series h2{font-family:"Didact Gothic",sans-serif;font-weight:400;font-size:15px;color:#7b6cc2;margin-bottom:8px}
.series h2.teal{color:var(--teal-dark)}
.series li{list-style:none;font-size:10px;height:26px;line-height:24px;border-bottom:1px dotted #bbb;padding-left:14px;position:relative;white-space:nowrap}
.series li:last-child{border:0}
.series li::before{content:"";position:absolute;left:3px;top:9px;border:3.5px solid transparent;border-left:4px solid #555}
.video-box{left:129px;top:733px;width:385px;height:263px;border:1px solid #ddd;border-radius:3px;box-shadow:0 1px 3px rgba(0,0,0,.15);padding:6px 11px}
.video-box h2{font-size:13px;font-family:"Didact Gothic",sans-serif;font-weight:400;color:var(--teal-dark);margin-bottom:6px}
.video-box h2 span{color:#7b6cc2}
.player{position:relative;width:362px;height:221px;background:#111}
.frame{position:absolute;left:12px;top:9px;width:338px;height:186px;background:linear-gradient(135deg,#7a6a3a,#b9a97a 45%,#4b5a58)}
.controls{position:absolute;left:0;bottom:0;width:100%;height:26px;background:#1c1c1c;border-top:3px solid #444;font-size:8px;color:#ddd;padding:7px 0 0 64px}
.controls::before{content:"";position:absolute;left:0;top:-3px;width:38px;height:3px;background:#d42020}

/* sidebar */
.card{left:545px;width:150px;border-radius:2px;padding:8px 10px}
.card h3{font-family:"Didact Gothic",sans-serif;font-weight:400;font-size:13.5px;color:#222;margin-bottom:8px;white-space:nowrap}
.contact{top:435px;height:210px;background:var(--panel)}
.field{width:131px;height:21px;background:var(--field);border:1px solid #ccc;border-radius:3px;font-size:10px;padding:4px 7px;margin-bottom:6px}
.field.area{height:53px}
.btn{display:inline-block;width:47px;height:20px;border:1px solid #aaa;border-radius:3px;background:linear-gradient(#fafafa,#ddd);font-size:10.5px;text-align:center;line-height:18px;color:#333}
.newsletter{top:664px;height:106px;background:var(--beige)}
.newsletter h3{margin-bottom:12px}
.tweet{top:790px;height:203px;background:var(--panel)}
.tweet h3{color:var(--tweet-blue)}
.bubble{width:133px;height:107px;background:var(--white);border:1px solid #ccc;border-radius:10px;padding:20px 7px 0;font-size:8.5px;line-height:11px;color:#555}
.bubble .meta{margin-top:18px;border-top:1px dotted #bbb;padding-top:6px;font-size:7.5px;color:#888;white-space:nowrap}
.bird{left:549px;top:937px;width:35px;height:40px;border-radius:50%;background:linear-gradient(#6fc0e6,#4fa84a)}
.tweet-btn{left:632px;top:946px;font-size:8.5px;display:flex;gap:4px}
.tweet-btn span{border:1px solid #bbb;border-radius:2px;background:#f5f5f5;padding:1px 4px}

/* footer */
.footer{left:0;top:1030px;width:825px;height:170px;background:linear-gradient(180deg,var(--footer),var(--footer-dark))}
.f-title{top:1051px;font-family:"Carlito",sans-serif;font-size:13px;font-weight:400;color:var(--white)}
.f-list{top:1073px;list-style:none;font-size:10.5px;color:#d6d0f0}
.f-list li{height:26px;line-height:14px;border-bottom:1px solid rgba(255,255,255,.12);white-space:nowrap}
.f-list li:last-child{border:0}
.f-list .sq{display:inline-block;width:16px;height:16px;border-radius:3px;background:#8fa9df;vertical-align:middle;margin-right:8px}
.map{left:460px;top:1076px;width:256px;height:93px;border-radius:3px;background:linear-gradient(90deg,#a9c2d8,#d9e2c8 60%,#cfd9e6);padding:5px 6px;font-size:10.5px;line-height:13.5px;color:#111}
.map .phone{margin-top:8px;font-size:10.5px}
.map .phone b{font-size:14px;font-weight:400}
.copy{right:109px;top:1180px;font-size:9px;color:var(--white)}
</style>
</head>
<body>

<header>
  <div class="abs brand"><span>Kali Rom</span><span class="brand-dot"></span></div>
  <div class="abs lang-label">Select Language:</div>
  <div class="abs lang-select">English</div>
  <div class="abs search">Search</div>
  <div class="abs follow">Follow Us:<span class="sq" aria-label="Facepage"></span><span class="sq" aria-label="Chirpline"></span><span class="sq" aria-label="Circlenet"></span></div>

  <nav class="abs nav">
    <a class="active" href="#">HOME</a><a href="#">COURSES</a><a href="#">LECTURER</a><a href="#">CONTACT US</a>
  </nav>
  <div class="abs call">
    <svg width="24" height="32" viewBox="0 0 24 32"><path d="M6 2c-3 1-5 4-4 9 2 8 7 15 14 19 3 1 5 0 6-2l-4-6-3 2c-3-2-6-7-7-11l3-2z" fill="#c8201e"/></svg>
    <div><div class="call-label">CALL US NOW!</div><div class="call-num">4793516270</div></div>
  </div>
</header>

<section class="abs slider">
  <div class="slide" role="img" aria-label="Rotating banner photo: smiling group of students outdoors">
    <div class="arrow prev"><svg width="8" height="12"><path d="M7 1L2 6l5 5" stroke="#fff" stroke-width="2" fill="none"/></svg></div>
    <div class="arrow next"><svg width="8" height="12"><path d="M1 1l5 5-5 5" stroke="#fff" stroke-width="2" fill="none"/></svg></div>
    <div class="caption">Neque porro quisquam est qui dolorem ipsum quia dolor sit amet...</div>
  </div>
</section>

<main>
  <div class="abs main"></div>
  <h1 class="abs h-section intro-title">What we do?</h1>
  <p class="abs intro">but also the leap into electronic typesetting, remaining essentially unchanged. It was popularised in the 1960s with the release of Lettrafix sheets containing Lorem Ipsum passages, and more recently with desktop publishing software like Quill PageSetter including versions of Lorem Ipsum. desktop publishing software like Quill PageSetter including versions</p>
  <a class="abs read-more" href="#">Read More...</a>

  <div class="abs series" style="left:129px;top:550px">
    <h2>CORE SERIES</h2>
    <ul><li>Lorem Ipsum is simpl</li><li>Dummy printing industry.</li><li>The industry's text.</li><li>Standard dummy unknown printer.</li><li>Text ever since then.</li></ul>
  </div>
  <div class="abs series" style="left:333px;top:550px">
    <h2 class="teal">TOP SERIES</h2>
    <ul><li>Lorem Ipsum is simpl</li><li>Dummy printing industry.</li><li>Typesetting industry.</li><li>Lorem Ipsum unknown.</li><li>The industry's text.</li></ul>
  </div>

  <div class="abs video-box">
    <h2>Latest <span>Video</span></h2>
    <div class="player">
      <div class="frame" role="img" aria-label="Video still: lecturer presenting a chart to a seated class"></div>
      <svg style="position:absolute;left:160px;top:82px" width="42" height="40" viewBox="0 0 42 40"><rect width="42" height="40" rx="6" fill="#d21f1f"/><path d="M15 10l14 10-14 10z" fill="#fff"/></svg>
      <div class="controls">0:14 / 2:57</div>
    </div>
  </div>

  <aside>
    <div class="abs card contact">
      <h3>Quick Contact</h3>
      <div class="field">Name:</div><div class="field">Email:</div><div class="field">Phone:</div><div class="field area">Massage:</div>
      <span class="btn">Submit</span>
    </div>
    <div class="abs card newsletter">
      <h3>Our Newsletter!</h3>
      <svg class="abs" style="left:107px;top:8px" width="34" height="26" viewBox="0 0 34 26"><rect x="1" y="5" width="30" height="20" fill="#eef2f8" stroke="#9ab"/><path d="M1 5l15 11 15-11" fill="none" stroke="#9ab"/></svg>
      <div class="field">Enter your email...</div>
      <span class="btn">Submit</span>
    </div>
    <div class="abs card tweet">
      <h3>Latest Tweet!</h3>
      <div class="bubble">Lorem but also the intoelectronic typesetting, reme ssentially into unchanged.<div class="meta">about 18 hours ago | reply | retweet</div></div>
    </div>
    <div class="abs bird" role="img" aria-label="Small bird mascot"></div>
    <div class="abs tweet-btn"><span>Tweet</span><span>6</span></div>
  </aside>
</main>

<footer>
  <div class="abs footer"></div>
  <h4 class="abs f-title" style="left:110px">Quick Links</h4>
  <ul class="abs f-list" style="left:110px;width:80px"><li>Home</li><li>Courses</li><li>Lectuere</li><li>Contact Us</li></ul>
  <h4 class="abs f-title" style="left:209px">Our Cources</h4>
  <ul class="abs f-list" style="left:209px;width:135px"><li>Lorem Ipsum is simply</li><li>including versions</li><li>industry's standard dummy</li><li>popularised</li></ul>
  <h4 class="abs f-title" style="left:363px">Follow Us</h4>
  <ul class="abs f-list" style="left:363px;top:1070px"><li><span class="sq"></span>Facepage</li><li><span class="sq"></span>Chirpline</li><li><span class="sq"></span>Circlenet</li></ul>
  <h4 class="abs f-title" style="left:460px">Contact Us</h4>
  <address class="abs map" role="img" aria-label="Location map of the teaching center" style="font-style:normal">
    Kali Rom AS,<br>Endodontic Teaching Center,<br>Fjeldstads vei 17C,<br>0371 Oslo, Norway.
    <div class="phone">Phone: <b>4793516270</b></div>
  </address>
  <p class="abs copy">Copyright © 2012 Dental Education. All Rights Reserved.</p>
</footer>

</body>
</html>
```